Spoke Haven and recovery web and app design

GPS enabled APP providing breakdown and assistance for cyclists by cyclists.
24 hour bicycle assist and recovery package for both road and off road cyclists.
First and only bicycle assist package whose aim is to get you back on your bike to complete your journey

I need the design package to give a website designer so they can build website and app. I have a logo done by my nephew which is the company logo but i need a full design package now.

Below is the website banner I have now and the logo

Reason: I am moving house today and have no internet till Tuesday so please extend deadline 5 days to allow everyone

Target Market(s)

Cyclists in the South East and London, and then all UK, includes MTB off road and road cyclists. Please see Wheelhomedirectx.co.uk as this was my pretotype website for market information.

Number of Pages Required

5+ page

Font styles to use
Other font styles liked:
• WHEELHOME DIRECT

Colors
ffcf3e
f04b51
f68d4c
faa54b
fbee3f
add136

Requirements
Must have
• Landing page, mechanical page, medical page, FAQ page, policy information page accessible by policy holder to update, lost password page, quote page, pay page, contact us page, all policy info must be accessible by Ringmoor Aid out operations room provider,
Nice to have
• Lots of great action cycling photos and very usable website

```html
<!DOCTYPE html>
<html lang="en">
<head>
<meta charset="utf-8">
<title>Wheelhome Direct — 24 Hour Bicycle Assistance</title>
<link rel="stylesheet" href="https://fonts.googleapis.com/css2?family=Oswald:wght@500&family=Roboto:ital,wght@0,400;0,500;1,400&display=swap">
<style>
:root{
  --red:#e9474d;
  --green:#a9cd36;
  --yellow:#f5c63c;
  --orange:#f68d4c;
  --ink:#555;
  --grey-band:#efefef;
  --footer:#333;
  --gold:#f3c137;
  --button:#3a3a3a;
}
*{box-sizing:border-box;margin:0;padding:0}
html,body{width:815px;height:1200px;overflow:hidden;background:#fff}
body{font-family:"Roboto",Arial,sans-serif;color:var(--ink);position:relative}

/* header */
.site-header{position:absolute;left:0;top:0;width:815px;height:67px;background:#fff}
.brand{position:absolute;left:51px;top:22px;display:flex;align-items:center;gap:10px}
.brand-dot{width:22px;height:22px;border-radius:50%;background:var(--red)}
.brand-name{font-family:"Oswald",sans-serif;font-weight:500;font-size:21px;color:#444;letter-spacing:.2px}
.main-nav{position:absolute;right:50px;top:29px;display:flex;gap:21px;font-size:9.6px;letter-spacing:.3px;color:#666}
.main-nav a{color:inherit;text-decoration:none;position:relative}
.main-nav a.active{color:var(--red)}
.main-nav a.active::after{content:"";position:absolute;left:-10px;right:-10px;top:17px;height:2px;background:var(--red)}

/* hero */
.hero{position:absolute;left:0;top:67px;width:815px;height:317px;
  background:linear-gradient(100deg,#7da3cf 0%,#a9c4e3 30%,#dde6ee 48%,#b9b96a 62%,#a8a24a 78%,#c6a13c 100%)}
.hero-title{position:absolute;left:0;right:0;top:92px;text-align:center;font-family:"Oswald",sans-serif;font-weight:500;
  font-size:32px;line-height:38px;color:#fff;text-shadow:0 2px 4px rgba(0,0,0,.35);letter-spacing:-.3px}
.hero-arrow{position:absolute;top:146px;left:50px}

/* download buttons */
.store-btn{position:absolute;height:36px;background:var(--button);border-radius:4px;color:#fff;
  display:flex;align-items:center;justify-content:center;gap:8px;font-size:14px;font-weight:500}
.store-btn-mark{width:10px;height:10px;background:#fff;border-radius:2px;flex:none}

/* welcome */
.section-title{font-size:15.5px;font-weight:400;color:var(--red);letter-spacing:.3px}
.welcome-title{position:absolute;left:0;right:0;top:412px;text-align:center}
.welcome-text{position:absolute;left:50px;width:716px;top:439px;text-align:center;font-size:9.6px;line-height:17.6px;color:#666}
.btn-read{position:absolute;left:365px;top:512px;width:86px;height:27px;background:var(--button);color:#fff;font-size:9.6px;font-weight:500;
  display:flex;align-items:center;justify-content:center;border-radius:2px}
.divider{position:absolute;left:110px;width:595px;top:566px;height:4px;border-radius:50%;
  background:radial-gradient(ellipse at center,rgba(0,0,0,.14),rgba(0,0,0,0) 70%)}

/* feature cards */
.feature{position:absolute;top:595px;width:225px;height:179px;color:#fff;text-align:center}
.feature-green{left:51px;background:var(--green)}
.feature-yellow{left:295px;background:var(--yellow)}
.feature-orange{left:541px;background:var(--orange)}
.feature-icon{position:absolute;left:75px;top:9px;width:75px;height:75px;border-radius:50%;background:#fff;display:flex;align-items:center;justify-content:center}
.feature h3{position:absolute;left:0;right:0;top:94px;font-size:16px;font-weight:400;letter-spacing:.5px}
.feature p{position:absolute;left:14px;right:14px;top:117px;font-size:9.4px;line-height:15.2px}

/* grey band */
.band{position:absolute;left:0;top:804px;width:815px;height:254px;background:var(--grey-band)}
.video-title{position:absolute;left:52px;top:832px}
.reviews-title{position:absolute;left:370px;top:832px}
.video{position:absolute;left:51px;top:862px;width:287px;height:164px;
  background:linear-gradient(160deg,#7a7a7a 0%,#b68a58 55%,#d6792f 85%,#5a3a20 100%)}
.play{position:absolute;left:124px;top:63px}
.review{position:absolute;left:370px;width:400px}
.avatar{position:absolute;left:0;top:0;width:48px;height:44px;background:linear-gradient(#dcd3c8,#b9a592)}
.stars{position:absolute;left:64px;top:2px}
.review p{position:absolute;left:64px;top:18px;width:336px;font-size:9.2px;line-height:15px;font-style:italic;color:#555}

/* download strip */
.download-title{position:absolute;left:138px;top:1083px;font-size:14.4px;font-weight:400;color:var(--red);letter-spacing:.3px}
.curve{position:absolute;left:348px;top:1096px}

/* footer */
.site-footer{position:absolute;left:0;top:1126px;width:815px;height:74px;background:var(--footer)}
.footer-nav{position:absolute;left:51px;top:16px;display:flex;gap:18px;font-size:8.4px;color:#ddd;letter-spacing:.3px}
.footer-mark{position:absolute;left:51px;top:44px;width:16px;height:16px;border-radius:50%;border:1.5px solid #ccc}
.copyright{position:absolute;left:87px;top:45px;font-size:8px;color:#aaa}
.touch{position:absolute;left:537px;top:32px;font-size:9.6px;font-weight:500;color:var(--gold)}
.social{position:absolute;top:24px;width:26px;height:26px;border-radius:50%;border:1.5px solid #bbb}
</style>
</head>
<body>

<header class="site-header">
  <div class="brand"><span class="brand-dot"></span><span class="brand-name">WHEELHOME DIRECT</span></div>
  <nav class="main-nav">
    <a class="active" href="#">HOME</a>
    <a href="#">ABOUT APPLICATION</a>
    <a href="#">HOW IT WORKS</a>
    <a href="#">REVIEWS</a>
    <a href="#">DOWNLOAD</a>
    <a href="#">CONTACT</a>
  </nav>
</header>

<section class="hero" role="img" aria-label="Action photo of a road cyclist and a mountain biker riding against sky and hillside">
  <svg class="hero-arrow" width="16" height="28" viewBox="0 0 16 28"><path d="M14 2 2 14l12 12" fill="none" stroke="#333" stroke-width="2"/></svg>
  <h1 class="hero-title">WE GIVES 24 HOUR ASSISTANCE AND RECOVERY<br>TO BICYCLE BREAKDOWNS</h1>
  <a class="store-btn" style="left:293px;top:193px;width:110px"><span class="store-btn-mark"></span>AppVault</a>
  <a class="store-btn" style="left:410px;top:193px;width:112px"><span class="store-btn-mark"></span>PlayBay</a>
</section>

<h2 class="section-title welcome-title">WELCOME TO WHEELHOME DIRECT</h2>
<p class="welcome-text">Aliquam molestie, mi et imperdiet euismod, dui purus auctor tellus, et interdum lacus lectus et ante. Sed accumsan sollicitudin sapien, sit amet adipiscing turpis gravida ac. In congue, neque ac lobortis volutpat, libero mauris varius mi, vitae suscipit ipsum ligula vitae risus. Duis aliquam nibh a dui iaculis viverra id a velit. Vivamus egestas risus in magna varius commodo. Sed semper viverra egestas. Etiam pretium porttitor lectus, vel ornare neque porta volutpat.</p>
<a class="btn-read">READ MORE</a>
<div class="divider"></div>

<article class="feature feature-green">
  <div class="feature-icon">
    <svg width="56" height="34" viewBox="0 0 56 34" fill="none" stroke="#444" stroke-width="2.2">
      <circle cx="11" cy="22" r="10"/><circle cx="45" cy="22" r="10"/>
      <path d="M11 22 20 7h18l7 15M20 7l8 15 10-15M28 22h-17M17 3h7M36 3l2 4"/>
    </svg>
  </div>
  <h3>SPOKE HAVEN</h3>
  <p>At Wheelhome Direct we want you and your bike to be in perfect working order so join us now..</p>
</article>
<article class="feature feature-yellow">
  <div class="feature-icon"></div>
  <h3>WHEELHOME DIRECT</h3>
  <p>GPS enabled APP providing breakdown and assistance for cyclists by cyclists. 24 hour bicycle assist and recovery package...</p>
</article>
<article class="feature feature-orange">
  <div class="feature-icon">
    <svg width="40" height="44" viewBox="0 0 40 44" fill="none" stroke="#444" stroke-width="2">
      <circle cx="20" cy="17" r="9"/><path d="M8 18v-3a12 12 0 0 1 24 0v3M8 14h-2v7h2zM32 14h2v7h-2zM32 21c0 5-4 7-10 7"/>
      <path d="M4 42c0-8 7-12 16-12s16 4 16 12z"/>
    </svg>
  </div>
  <h3>ASSISTANCE PACKAGE</h3>
  <p>Join our premium assistance package and an enhanced first aid kit specifically designed cycling injuries ..</p>
</article>

<section class="band"></section>
<h2 class="section-title video-title">WATCH HOW IT WORKS</h2>
<div class="video" role="img" aria-label="Video still of a mountain bike wheel on a dusty trail at sunset">
  <svg class="play" width="38" height="38" viewBox="0 0 38 38"><circle cx="19" cy="19" r="16" fill="none" stroke="#fff" stroke-width="3.5"/><path d="M15 11v16l12-8z" fill="#fff"/></svg>
</div>

<h2 class="section-title reviews-title">CUSTOMER REVIEWS</h2>
<div class="review" style="top:862px">
  <div class="avatar" role="img" aria-label="Customer portrait"></div>
  <svg class="stars" width="70" height="9" viewBox="0 0 70 9" fill="#f0b323"><path id="st" d="M4.5 0 5.6 3.3H9L6.3 5.3 7.3 8.6 4.5 6.6 1.7 8.6 2.7 5.3 0 3.3h3.4z"/><use href="#st" x="15"/><use href="#st" x="30"/><use href="#st" x="45"/><use href="#st" x="60"/></svg>
  <p>Aliquam molestie, mi et imperdiet euismod, dui purus auctor tellus, et interdum lacus lectus et ante. Sed accumsan sollicitudin sapien..</p>
</div>
<div class="review" style="top:922px">
  <div class="avatar" role="img" aria-label="Customer portrait"></div>
  <svg class="stars" width="70" height="9" viewBox="0 0 70 9" fill="#f0b323"><use href="#st"/><use href="#st" x="15"/><use href="#st" x="30"/><use href="#st" x="45"/><use href="#st" x="60"/></svg>
  <p>Aliquam molestie, mi et imperdiet euismod, dui purus auctor tellus, et interdum lacus lectus et ante. Sed accumsan sollicitudin sapien..</p>
</div>
<div class="review" style="top:982px">
  <div class="avatar" role="img" aria-label="Customer portrait"></div>
  <svg class="stars" width="70" height="9" viewBox="0 0 70 9" fill="#f0b323"><use href="#st"/><use href="#st" x="15"/><use href="#st" x="30"/><use href="#st" x="45"/><use href="#st" x="60"/></svg>
  <p>Aliquam molestie, mi et imperdiet euismod, dui purus auctor tellus, et interdum lacus lectus et ante. Sed accumsan sollicitudin sapien..</p>
</div>

<h2 class="download-title">APP AVAILABLE TO DOWNLOADS</h2>
<svg class="curve" width="84" height="20" viewBox="0 0 84 20" fill="none" stroke="#555" stroke-width="1"><path d="M2 12c25 8 55 4 78-10M73 2h7l-2 6"/></svg>
<a class="store-btn" style="left:443px;top:1074px;width:109px"><span class="store-btn-mark"></span>AppVault</a>
<a class="store-btn" style="left:560px;top:1074px;width:112px"><span class="store-btn-mark"></span>PlayBay</a>

<footer class="site-footer">
  <nav class="footer-nav"><span>HOME</span><span>ABOUT APPLICATION</span><span>HOW IT WORKS</span><span>REVIEWS</span><span>DOWNLOAD</span><span>CONTACT</span></nav>
  <span class="footer-mark"></span>
  <span class="copyright">Copyright © 2015. Company Name All Right Reserved</span>
  <span class="touch">GET IN TOUCH</span>
  <span class="social" style="left:612px"></span>
  <span class="social" style="left:643px"></span>
  <span class="social" style="left:674px"></span>
  <span class="social" style="left:705px"></span>
  <span class="social" style="left:736px"></span>
</footer>

</body>
</html>
```